Market Intelligence Modules

Take the existing power point and add graphics to each slide and use photos and graphics to create a power point presentation that has the look and feel of a high tech company / research - with a theme of commercial real estate. To learn more about what the company does you can go to www.kovanstel.com.

Target Market(s)

Target market are financial institutions and commercial real estate developers - going for high tech research look and feel and showing commercial real estate. ONLY commercial real estate.

Industry/Entity Type

Real Estate

Requirements
Must have
• Must have Brindlequay logo and must communicate that Brindlequay can process large amounts of data and analytics. Each slide should have some type of image that represents data or commercial real estate.
Should not have
• No blank white slides.

```html
<!DOCTYPE html>
<html lang="en">
<head>
<meta charset="utf-8">
<title>The Zettabyte Era</title>
<link href="https://fonts.googleapis.com/css2?family=Arimo:wght@400;700&display=swap" rel="stylesheet">
<style>
  :root {
    --green: #3a9e2a;
    --tan: #cfc3ad;
    --text: #3c3c3c;
    --blue: #1f7fc4;
    --faint: #dde3e8;
    --row-line: #d9d9d9;
    --white: #ffffff;
    --bg-light: #f3f4f4;
    --bg-mid: #dcdfe0;
  }
  * { margin: 0; padding: 0; box-sizing: border-box; }
  html, body { width: 1200px; height: 900px; overflow: hidden; background: var(--white); }
  body { font-family: "Arimo", Arial, sans-serif; color: var(--text); position: relative; }

  .slide-title {
    position: absolute; left: 132px; top: 48px;
    font-size: 37px; font-weight: 700; color: var(--green);
  }
  .title-rule {
    position: absolute; left: 0; top: 104px; width: 422px; height: 14px;
    background: var(--tan);
  }
  .backdrop {
    position: absolute; left: 0; top: 134px; width: 1200px; height: 692px;
    background: linear-gradient(100deg, var(--bg-light) 0%, var(--bg-mid) 45%, var(--bg-light) 75%, #e6e8e9 100%);
  }

  .info-panel {
    position: absolute; left: 63px; top: 210px; width: 457px; height: 531px;
    background: rgba(255,255,255,0.82);
    border: 1px solid rgba(255,255,255,0.9);
    padding: 20px 30px 0 30px;
  }
  .info-panel h2 {
    font-size: 33px; font-weight: 700; color: var(--green); margin-bottom: 22px;
  }
  .facts { list-style: none; }
  .facts li {
    position: relative; padding-left: 48px;
    font-size: 21px; line-height: 35px; margin-bottom: 27px;
  }
  .facts li svg { position: absolute; left: 14px; top: 10px; }

  .data-table {
    position: absolute; left: 570px; top: 352px; width: 612px; height: 388px;
    background: var(--white);
    padding: 24px 18px 0 18px;
  }
  .data-table h3 {
    font-size: 15px; font-weight: 700; color: var(--text); letter-spacing: 0.3px;
    padding-left: 6px; padding-bottom: 6px; border-bottom: 1px solid var(--row-line);
  }
  .unit-row {
    display: flex; align-items: center; height: 44.6px;
    border-bottom: 2px solid var(--row-line);
    font-size: 23px;
  }
  .unit-row .unit { width: 198px; padding-left: 16px; color: var(--text); }
  .unit-row .value { font-weight: 700; color: var(--blue); letter-spacing: 0.2px; }
  .unit-row .value span { color: var(--faint); }
  .source {
    text-align: right; font-size: 8px; color: #aaa; letter-spacing: 0.5px; padding-top: 6px;
  }

  .footer-copy {
    position: absolute; left: 16px; top: 853px; font-size: 20px; color: #222;
  }
  .brand {
    position: absolute; right: 22px; top: 843px;
    font-size: 37px; font-weight: 700; color: var(--green); letter-spacing: -0.5px;
  }
</style>
</head>
<body>
  <h1 class="slide-title">The Zettabyte Era</h1>
  <div class="title-rule"></div>

  <div class="backdrop" role="img" aria-label="Faded photo of a modern commercial building interior with escalators and a glass ceiling"></div>

  <section class="info-panel">
    <h2>What is a zettabyte?</h2>
    <ul class="facts">
      <li><svg width="14" height="16" viewBox="0 0 14 16"><path d="M2 1 L11 8 L2 15" fill="none" stroke="#3a9e2a" stroke-width="4"/></svg>One zettabyte of data allows you to stack books from Earth to Pluto 20 times (72 billion miles)</li>
      <li><svg width="14" height="16" viewBox="0 0 14 16"><path d="M2 1 L11 8 L2 15" fill="none" stroke="#3a9e2a" stroke-width="4"/></svg>If one gigabyte of data were a cup of coffee a zettabyte would equal the Great Wall of China</li>
      <li><svg width="14" height="16" viewBox="0 0 14 16"><path d="M2 1 L11 8 L2 15" fill="none" stroke="#3a9e2a" stroke-width="4"/></svg>In 2015 all internet traffic will exceed one zettabyte of data - 540,000 time increase from 2003</li>
    </ul>
  </section>

  <section class="data-table">
    <h3>WHAT'S A ZETTABYTE?</h3>
    <div class="unit-row"><div class="unit">1 kilobyte</div><div class="value">1,000<span>,000,000,000,000,000,000</span></div></div>
    <div class="unit-row"><div class="unit">1 megabyte</div><div class="value">1,000,000<span>,000,000,000,000,000</span></div></div>
    <div class="unit-row"><div class="unit">1 gigabyte</div><div class="value">1,000,000,000<span>,000,000,000,000</span></div></div>
    <div class="unit-row"><div class="unit">1 terabyte</div><div class="value">1,000,000,000,000<span>,000,000,000</span></div></div>
    <div class="unit-row"><div class="unit">1 petabyte</div><div class="value">1,000,000,000,000,000<span>,000,000</span></div></div>
    <div class="unit-row"><div class="unit">1 exabyte</div><div class="value">1,000,000,000,000,000,000<span>,000</span></div></div>
    <div class="unit-row"><div class="unit">1 zettabyte</div><div class="value">1,000,000,000,000,000,000,000</div></div>
    <div class="source">SOURCE: NEXORA</div>
  </section>

  <div class="footer-copy">Copyright text here</div>
  <div class="brand">Brindlequay</div>
</body>
</html>
```